Change of Address Card

We are fertility physicians in New York . Need a change of address postcard .

The front should be colorful
contain the statement " we are moving!"
and the names Marcus Tolleson MD, Helen Brisco MD

Also the front should contain the drawing of a sperm with either wings or wheeels or whatever your creativity suggests as long as it is not vulgar ( we are doctors !)

The back should contain
the address area and stamp area
and a text area
and possibly a recall of the drawing in front.
use same font

text below

Dear Friends and Colleagues

Marcus and Helen are relocating their fertility practice to a new location on 418 West 91st Street, Suite 2207, New York NY 10024
Please take note of our new phone number
Our New phone Number is 212-640-5193

Thank you for your support!

Target Market(s)

this is a card that goes to physicians

Industry/Entity Type

It Support

Requirements
Must have
• fit standard postcard size
Rectangular
At least 3-1/2 inches high x 5 inches long x 0.007 inch thick
No more than 4-1/4 inches high x 6 inches long x 0.016 inches thick
will not be mailed in an envelope

```html
<!DOCTYPE html>
<html lang="en">
<head>
<meta charset="utf-8">
<title>We Are Moving – Change of Address Postcard</title>
<link rel="stylesheet" href="https://fonts.googleapis.com/css2?family=Questrial&display=swap">
<style>
  :root {
    --page-bg: #efece6;
    --card-edge: #f4f8fa;
    --frame-teal: #2f89a4;
    --panel-blue: #dbedf5;
    --ink-teal: #2a8aa8;
    --ink-dark: #1c1c1c;
    --rule-grey: #6d6d6d;
    --art-cream: #ece0b4;
    --art-sand: #d9c98f;
  }
  * { box-sizing: border-box; margin: 0; padding: 0; }
  html, body {
    width: 1200px;
    height: 1020px;
    overflow: hidden;
    background: var(--page-bg);
    font-family: "Questrial", "Century Gothic", sans-serif;
    color: var(--ink-teal);
  }
  .canvas { position: relative; width: 1200px; height: 1020px; }

  .postcard {
    position: absolute;
    background: var(--card-edge);
    padding: 10px;
    box-shadow: 0 2px 6px rgba(0,0,0,0.18);
  }
  .postcard__frame {
    width: 100%;
    height: 100%;
    background: var(--frame-teal);
    padding: 12px;
  }
  .postcard__panel {
    position: relative;
    width: 100%;
    height: 100%;
    background: var(--panel-blue);
    border-radius: 12px;
  }
  .postcard--front { left: 53px; top: 40px; width: 701px; height: 453px; }
  .postcard--back  { left: 438px; top: 524px; width: 734px; height: 454px; }

  .mascot-art {
    position: absolute;
    border-radius: 40% 55% 50% 45%;
    background: radial-gradient(ellipse at 30% 50%, var(--art-cream) 0%, var(--art-sand) 70%, rgba(217,201,143,0) 100%);
  }

  /* Front */
  .front__art { left: 177px; top: 16px; width: 300px; height: 180px; }
  .front__headline {
    position: absolute; left: 0; right: 0; top: 205px;
    text-align: center; font-size: 41px; font-weight: 400; letter-spacing: 0.3px;
  }
  .front__names {
    position: absolute; left: 0; right: 0; top: 272px;
    text-align: center; font-size: 28px; font-weight: 400; letter-spacing: 0.2px;
  }

  /* Back – positions relative to the panel */
  .back__art { left: 34px; top: 20px; width: 64px; height: 46px; }
  .back__headline { position: absolute; left: 105px; top: 27px; font-size: 24px; font-weight: 400; }
  .back__greeting { position: absolute; left: 38px; top: 93px; font-size: 17px; }
  .back__message {
    position: absolute; left: 80px; top: 128px; width: 228px;
    font-size: 17px; line-height: 20px;
  }
  .back__signoff { position: absolute; left: 43px; top: 320px; font-size: 17px; }
  .back__divider {
    position: absolute; left: 327px; top: 18px; width: 2px; height: 362px;
    background: var(--ink-dark);
  }
  .back__stamp {
    position: absolute; left: 574px; top: 8px; width: 72px; height: 82px;
    border: 2px solid var(--ink-dark);
  }
  .back__addressee { position: absolute; left: 372px; top: 147px; font-size: 17px; color: var(--ink-dark); }
  .address-lines { position: absolute; left: 367px; top: 0; width: 276px; height: 100%; }
  .address-lines__rule {
    position: absolute; left: 0; width: 100%; height: 0;
    border-top: 1.5px solid var(--rule-grey);
  }
</style>
</head>
<body>
<main class="canvas">

  <section class="postcard postcard--front">
    <div class="postcard__frame">
      <div class="postcard__panel">
        <div class="mascot-art front__art" role="img" aria-label="Cartoon of a smiling winged sperm character flying"></div>
        <h1 class="front__headline">we are moving!</h1>
        <p class="front__names">Marcus Tolleson MD, Helen Brisco MD</p>
      </div>
    </div>
  </section>

  <section class="postcard postcard--back">
    <div class="postcard__frame">
      <div class="postcard__panel">
        <div class="mascot-art back__art" role="img" aria-label="Small version of the winged sperm character"></div>
        <h2 class="back__headline">we are moving!</h2>
        <p class="back__greeting">Dear Friends and Colleagues,</p>
        <p class="back__message">Marcus and Helen are relocating their fertility practice to a new location on 418 West 91st Street, Suite 2207, New York NY 10024<br>Please take note of Our New phone Number is 212-640-5193</p>
        <p class="back__signoff">Thankingyou!</p>

        <div class="back__divider"></div>
        <div class="back__stamp" aria-label="Stamp area"></div>
        <p class="back__addressee">To,</p>
        <div class="address-lines">
          <div class="address-lines__rule" style="top:208px"></div>
          <div class="address-lines__rule" style="top:251px"></div>
          <div class="address-lines__rule" style="top:293px"></div>
          <div class="address-lines__rule" style="top:329px"></div>
          <div class="address-lines__rule" style="top:369px"></div>
        </div>
      </div>
    </div>
  </section>

</main>
</body>
</html>
```